Elegant sophisticated Invitation Design in A5

"Amber Hours of Vellmoor"
We are after an invitation A5 portrait size. It is for an outdoor event for a 4 course dinner. It needs to display high class, elegance and sophistication. We like the idea of having stars or reflections on the water (as per attached images we found on findora)

Text and logo are attached. The file needs to be supplied to use as psd file and needs to be 300dpi at least as the invitation will be printed.

We would like dark colours, black, and sparkles/stars.

The main focus is elegance!

Logos and text are attached.

Target Market(s)

Upper class, business men and women, Suit and tie event

Industry/Entity Type

Event

Font styles to use
Decorative
Script

Colors
fffefe
000000

Requirements
Must have
• The element of Water and stars or sparkles. It needs to speak elegance throughout. The fonts chosen need to be soft and elegant. The logo attached must be used either with the diamond or the standard version a mono version can also be used. Open for designers ideas.
Should not have
• Bold and bulky fonts it needs to be soft

```html
<!DOCTYPE html>
<html lang="en">
<head>
<meta charset="utf-8">
<title>Le Banquet – Amber Hours of Vellmoor</title>
<link href="https://fonts.googleapis.com/css2?family=Great+Vibes&family=Open+Sans:ital,wght@0,400;0,600;1,400&display=swap" rel="stylesheet">
<style>
  :root {
    --ink: #000000;
    --paper: #fffefe;
    --gold: #e8cf3a;
    --gold-deep: #b89a1c;
    --sky-top: #0a1a5c;
    --sky-mid: #1c3aa8;
    --sky-low: #25389a;
    --sea: #0b1230;
    --palm: #0c1029;
  }
  * { margin: 0; padding: 0; box-sizing: border-box; }
  html, body { width: 922px; height: 1200px; overflow: hidden; background: #d9d9d9; }
  .invitation {
    position: relative; width: 922px; height: 1200px; overflow: hidden;
    font-family: "Open Sans", sans-serif; color: var(--paper);
    background: var(--ink);
  }
  .night-sky {
    position: absolute; inset: 0;
    background:
      radial-gradient(ellipse at 45% 55%, rgba(70,110,230,.55), transparent 60%),
      linear-gradient(180deg, var(--sky-top) 0%, var(--sky-mid) 45%, var(--sky-low) 75%, var(--sea) 88%);
  }
  .palm-silhouette {
    position: absolute; left: 0; top: 470px; width: 420px; height: 620px;
    background: radial-gradient(ellipse at 35% 28%, rgba(12,16,41,.92) 0%, rgba(12,16,41,.7) 35%, transparent 65%);
  }
  .shoreline {
    position: absolute; left: 0; right: 0; bottom: 0; height: 200px;
    background: linear-gradient(180deg, transparent 0%, var(--ink) 40%);
  }
  .header-band {
    position: absolute; top: 0; left: 0; right: 0; height: 96px; background: var(--ink);
    display: flex; align-items: center; justify-content: center;
  }
  .header-band p {
    color: var(--gold); font-size: 27px; letter-spacing: 3.5px; text-transform: uppercase;
  }
  .vip-badge {
    position: absolute; left: 670px; top: 132px; width: 150px; height: 150px; border-radius: 50%;
    border: 2px solid rgba(255,255,255,.85);
    box-shadow: 0 0 14px rgba(200,210,255,.8), inset 0 0 12px rgba(200,210,255,.5);
    text-align: center; color: rgba(235,238,255,.92);
  }
  .vip-badge .vip { display: block; font-size: 56px; line-height: 1; margin-top: 26px; letter-spacing: 2px; }
  .vip-badge .dinner { display: block; font-size: 21px; letter-spacing: 1px; }
  .event-title {
    position: absolute; left: 40px; top: 210px; width: 780px; text-align: center;
    font-family: "Great Vibes", cursive; font-weight: 400; font-size: 150px; line-height: 1;
    color: var(--gold);
    text-shadow: 0 3px 6px rgba(0,0,0,.6);
  }
  .event-subtitle {
    position: absolute; left: 95px; top: 392px; width: 690px; padding: 6px 0;
    border-top: 2px solid var(--gold); border-bottom: 2px solid var(--gold);
    text-align: center; font-size: 38px; letter-spacing: 3px; text-transform: uppercase;
  }
  .details {
    position: absolute; left: 340px; width: 480px; text-align: center;
    font-size: 22px; line-height: 1.42; color: rgba(255,254,254,.93);
  }
  .details h2 {
    color: var(--gold); font-weight: 400; font-size: 31px; letter-spacing: 1px; text-transform: uppercase;
    margin-bottom: 2px;
  }
  .details.when { top: 528px; }
  .details.offer { top: 748px; }
  .details .spaced { letter-spacing: 3px; }
  .details em { font-style: italic; }
  .host-mark {
    position: absolute; left: 311px; top: 1010px; width: 300px; text-align: center;
  }
  .host-mark .dot {
    display: block; width: 46px; height: 46px; border-radius: 50%;
    background: var(--gold); margin: 0 auto 14px;
  }
  .host-mark .name {
    display: block; font-size: 34px; font-weight: 400; line-height: 1.15; color: var(--paper);
  }
</style>
</head>
<body>
<main class="invitation">
  <div class="night-sky" role="img" aria-label="Starry night sky with milky way over a calm sea"></div>
  <div class="palm-silhouette" role="img" aria-label="Silhouette of a palm tree against the night sky"></div>
  <div class="shoreline" role="img" aria-label="Dark shoreline hills along the water"></div>

  <header class="header-band"><p>Marrowind Northern Coast’s Inaugural</p></header>

  <div class="vip-badge"><span class="vip">VIP</span><span class="dinner">DINNER</span></div>

  <h1 class="event-title">Le Banquet</h1>
  <p class="event-subtitle">Amber Hours of Vellmoor</p>

  <section class="details when">
    <h2>Saturday 17th July 2017</h2>
    <p>HARBOURSIDE GALLERY PARK</p>
    <p>Calder Street, South Vellmoor</p>
    <p>Building accessible housing for people<br>with disability in North Queensland</p>
  </section>

  <section class="details offer">
    <h2 class="spaced">By Invitation</h2>
    <p>Four course dinner exclusively crafted by<br><em>A Grain of Brine Restaurant</em></p>
    <p>Beautiful wines and fine beers included</p>
    <p>Live Entertainment</p>
  </section>

  <div class="host-mark">
    <span class="dot"></span>
    <span class="name">Marrowind</span>
  </div>
</main>
</body>
</html>
```